SipNOW Business Cards

Hi designers!

Here's some background on our start-up and this project:

SipNOW is a website that will allow users to order alcohol from nearby liquor stores and have it delivered to their homes in minutes. We are really excited to work on creating the best online, alcohol purchasing experience for the users.

So why SipNOW? We like to think of ourselves as that great friend who will get alcohol for you because he happens to have a car. We help you drink in with your friends, family, or guests. Our site will target students and young professionals (of drinking age) who are comfortable buying things online or through apps. We don't see this service as a luxury, VIP, or niche service in the least; instead, we think of us as a relaxed, service-driven start-up that believes in simple design and transparent .

Now, we want a business card that incorporates our newly acquired logo design and some complimenting colors and fonts. Feel free to do it single or double sided, although I'm a sucker for double...

If you happen to have any questions, want to throw some ideas around, or just want some feedback- email me at marco@sipnow.example.

Marco Tessin
Founder

Industry/Entity Type

Business

Requirements
Must have
• Name, Position, Email, Cell-phone

No address, no fax, no land-line.

```html
<!DOCTYPE html>
<html lang="en">
<head>
<meta charset="utf-8">
<title>SipNOW Business Cards</title>
<link rel="stylesheet" href="https://fonts.googleapis.com/css2?family=Arvo:wght@400;700&family=Montserrat:wght@400;600&display=swap">
<style>
  :root {
    --backdrop: #2b2b2b;
    --brand-yellow: #f4b71b;
    --brand-yellow-deep: #e0a512;
    --pattern-cream: #f8f1da;
    --card-white: #ffffff;
    --ink: #3a3a3a;
    --ink-dark: #1e1e1e;
  }
  * { margin: 0; padding: 0; box-sizing: border-box; }
  html, body {
    width: 1200px;
    height: 900px;
    overflow: hidden;
    background: var(--backdrop);
  }
  .canvas {
    width: 1200px;
    height: 900px;
    display: flex;
    flex-direction: column;
    align-items: center;
    justify-content: center;
    gap: 44px;
  }
  .card {
    position: relative;
    width: 560px;
    height: 320px;
    overflow: hidden;
  }

  /* Back side: contact details */
  .card-back { background: var(--card-white); }
  .bottle-pattern {
    position: absolute;
    inset: 0 0 110px 0;
    background: var(--pattern-cream);
  }
  .bottle-illustration {
    position: absolute;
    right: 0;
    top: 28px;
    width: 250px;
    height: 84px;
    background: linear-gradient(180deg, var(--brand-yellow) 0%, var(--brand-yellow-deep) 100%);
    border-radius: 42px 0 0 42px;
  }
  .contact-block {
    position: absolute;
    left: 40px;
    right: 40px;
    top: 128px;
    color: var(--ink);
  }
  .person-name {
    font-family: 'Arvo', serif;
    font-weight: 400;
    font-size: 32px;
    line-height: 1;
    color: var(--ink);
  }
  .person-role {
    font-family: 'Montserrat', sans-serif;
    font-weight: 400;
    font-size: 14px;
    letter-spacing: 4px;
    color: var(--brand-yellow);
    margin-top: 6px;
  }
  .contact-lines {
    margin-top: 38px;
    font-family: 'Arvo', serif;
    font-size: 18px;
    line-height: 1.55;
    color: var(--ink-dark);
  }
  .contact-row {
    display: flex;
    justify-content: space-between;
  }

  /* Front side: brand */
  .card-front {
    background: var(--brand-yellow);
    display: flex;
    align-items: center;
    justify-content: center;
    gap: 22px;
  }
  .brand-dot {
    width: 44px;
    height: 44px;
    border-radius: 50%;
    background: var(--card-white);
  }
  .brand-name {
    font-family: 'Arvo', serif;
    font-weight: 700;
    font-size: 88px;
    line-height: 1;
    color: var(--ink-dark);
  }
</style>
</head>
<body>
  <main class="canvas">
    <section class="card card-back">
      <div class="bottle-pattern" role="img" aria-label="Faint repeating pattern of small bottle silhouettes"></div>
      <div class="bottle-illustration" role="img" aria-label="Large yellow bottle silhouette lying on its side"></div>
      <div class="contact-block">
        <p class="person-name">Marco Tessin</p>
        <p class="person-role">FOUNDER</p>
        <div class="contact-lines">
          <div class="contact-row">
            <p class="contact-phone">555.018.4470</p>
            <p class="contact-web">sipnow.example</p>
          </div>
          <p class="contact-email">marco@sipnow.example</p>
        </div>
      </div>
    </section>

    <section class="card card-front">
      <span class="brand-dot"></span>
      <p class="brand-name">SipNOW</p>
    </section>
  </main>
</body>
</html>
```